Stationery Design Project

We are a start up wine business based in Sydney Australia. We already have a logo and are in the process of completing our website. We require our logo to be cleverly and artfully incorporated into our stationary requirements. Which will initially begin with a company letter head.
As we desire consistency across our brand, we will also be wanting to develop banner advertisements and brochure with the same "look".
If outstanding we move design brief to banner advertisement for web and banner of the website itself.
Target Market(s)
Older wealthy predominantly male demographic
Industry/Entity Type
Business
Look and feel

```html
<!DOCTYPE html>
<html lang="en">
<head>
<meta charset="utf-8">
<title>Vintage Crest International — Business Cards</title>
<link rel="stylesheet" href="https://fonts.googleapis.com/css2?family=Questrial&display=swap">
<style>
  :root {
    --page: #e7e5e2;
    --brown: #8b5a2b;
    --band-1: #a8743f;
    --band-2: #c49a68;
    --band-3: #d7b78f;
    --band-4: #e4cdb1;
    --cream: #ece0d3;
    --cream-light: #f1e8de;
    --accent: #b5733a;
    --ink: #3d2a1a;
    --white: #ffffff;
    --card-w: 640px;
    --card-h: 366px;
  }
  * { box-sizing: border-box; margin: 0; padding: 0; }
  html, body { width: 1200px; height: 880px; overflow: hidden; }
  body {
    background: var(--page);
    font-family: "Questrial", "Century Gothic", sans-serif;
    display: flex;
    flex-direction: column;
    align-items: center;
    justify-content: center;
    gap: 56px;
  }
  .card {
    position: relative;
    width: var(--card-w);
    height: var(--card-h);
    background: var(--brown);
    overflow: hidden;
    box-shadow: 0 6px 18px rgba(0,0,0,0.18);
  }
  .card__bands { position: absolute; inset: 0; width: 100%; height: 100%; }

  .brand {
    position: absolute;
    display: flex;
    align-items: center;
    gap: 12px;
    color: var(--white);
    font-size: 26px;
    line-height: 1.15;
    letter-spacing: 0.02em;
  }
  .brand__dot {
    width: 22px; height: 22px;
    border-radius: 50%;
    background: var(--white);
    flex: none;
  }

  /* brand side */
  .card--brand .brand { left: 64px; top: 96px; width: 260px; }
  .card--brand .brand-web {
    position: absolute;
    left: 64px; top: 226px;
    color: var(--white);
    font-size: 15px;
    letter-spacing: 0.06em;
  }

  /* contact side */
  .card--contact .brand { right: 48px; bottom: 62px; width: 230px; }
  .contact {
    position: absolute;
    left: 70px; top: 48px;
    color: var(--ink);
  }
  .contact__name { color: var(--accent); font-size: 24px; }
  .contact__role { font-size: 14px; margin-top: 2px; }
  .contact__list { list-style: none; margin-top: 26px; font-size: 15px; line-height: 1.55; }
  .contact__label { color: var(--accent); display: inline-block; width: 52px; }
</style>
</head>
<body>

  <section class="card card--brand" aria-label="Business card, brand side">
    <svg class="card__bands" viewBox="0 0 640 366" aria-hidden="true">
      <circle cx="660" cy="520" r="330" fill="var(--band-1)"/>
      <circle cx="660" cy="520" r="290" fill="var(--band-2)"/>
      <circle cx="660" cy="520" r="255" fill="var(--band-3)"/>
      <circle cx="660" cy="520" r="222" fill="var(--band-4)"/>
      <circle cx="660" cy="520" r="190" fill="var(--cream)"/>
    </svg>
    <div class="brand">
      <span class="brand__dot"></span>
      <span class="brand__name">Vintage Crest International</span>
    </div>
    <p class="brand-web">www.vintagecrest.com.au</p>
  </section>

  <section class="card card--contact" aria-label="Business card, contact side">
    <svg class="card__bands" viewBox="0 0 640 366" aria-hidden="true">
      <circle cx="110" cy="-40" r="420" fill="var(--band-1)"/>
      <circle cx="110" cy="-40" r="395" fill="var(--band-2)"/>
      <circle cx="110" cy="-40" r="372" fill="var(--band-3)"/>
      <circle cx="110" cy="-40" r="350" fill="var(--band-4)"/>
      <circle cx="110" cy="-40" r="328" fill="var(--cream)"/>
      <circle cx="110" cy="-40" r="300" fill="var(--cream-light)"/>
    </svg>
    <div class="contact">
      <p class="contact__name">Clara Whitfield</p>
      <p class="contact__role">Position</p>
      <ul class="contact__list">
        <li><span class="contact__label">tel :</span>0400 555 0100</li>
        <li><span class="contact__label">fax :</span>0400 555 0199</li>
        <li><span class="contact__label">email :</span>hello@vintagecrest.com.au</li>
        <li><span class="contact__label">web :</span>www.vintagecrest.com.au</li>
      </ul>
    </div>
    <div class="brand">
      <span class="brand__dot"></span>
      <span class="brand__name">Vintage Crest International</span>
    </div>
  </section>

</body>
</html>
```